Horseracing 8 page brochure - tight turnaround, deadline tomorrow 12GMT

Hi - we have a brochure already drafted for our annual open day at our horseracing stables in England, but it needs a professional design please! The design should convey that this is a smart, professional yard. We brand in a dark blue (as seen on the logo on the back page) and shades of blue. We have a range of other landscape / action photos available. This needs an almost instant turnaround please

Target Market(s)

Racehorse owners - current and prospective. High net worth / socio economic group

Industry/Entity Type

It Professional

Other font styles liked:
• As per 'Rob Dawes' text

Colors
0255a3
3176b5
85abd2
cedeed

Requirements
Must have
• All text and images in publisher file provided below. Other photos are optional for space filling / backrounds

```html
<!DOCTYPE html>
<html lang="en">
<head>
<meta charset="utf-8">
<title>Ashcombe Racing – 2016 Open Day</title>
<link rel="stylesheet" href="https://fonts.googleapis.com/css2?family=Lato:wght@400;700&family=EB+Garamond:wght@400;500&display=swap">
<style>
:root{
  --navy:#0a4a85;
  --navy-deep:#063c70;
  --sky:#5eb4e8;
  --cell:#cfe6f6;
  --heading:#2d2f86;
  --ink:#2b2b2b;
  --page-edge:#dcdcdc;
}
*{box-sizing:border-box;margin:0;padding:0}
html,body{width:1200px;height:900px;overflow:hidden;background:#fff}
body{position:relative;font-family:"Lato",sans-serif;color:var(--ink)}
.page{position:absolute;top:90px;height:720px;background:#fff;border:1px solid var(--page-edge);overflow:hidden}
.page--left{left:45px;width:556px}
.page--right{left:600px;width:557px}
.shapes{position:absolute;inset:0}
.portrait{position:absolute;left:55px;top:27px;width:88px;height:88px;border:4px solid #fff;border-radius:7px;background:linear-gradient(160deg,#b9cbb5 0%,#9fae8c 45%,#5a6f86 100%);box-shadow:0 0 0 1px #eee}
.brand{position:absolute;top:38px;display:flex;align-items:center;gap:4px;font-weight:700;font-size:9px;color:var(--navy-deep);letter-spacing:.02em}
.brand__dot{width:8px;height:8px;border-radius:50%;background:var(--navy-deep)}
.page--left .brand{left:450px}
.page--right .brand{left:440px}
.welcome{position:absolute;left:45px;top:116px;width:460px}
.welcome__title{font-family:"EB Garamond",serif;font-weight:500;font-size:17px;color:var(--heading);margin-bottom:6px}
.welcome__body p{font-size:7.3px;line-height:11.1px;margin-bottom:11.1px}
.welcome__body sup{font-size:5px}
.signature{position:absolute;left:275px;top:648px;width:100px;height:30px;background:#e9e8f6;border-radius:3px}
.stable-list{position:absolute;left:83px;top:90px;width:416px;height:566px;background:linear-gradient(#85c6ee 0%,#bfe0f5 55%,#f4f9fd 100%)}
.stable-list__head{display:grid;grid-template-columns:196px 196px;margin-left:12px;height:23px;align-items:center;font-family:"EB Garamond",serif;font-size:11px;color:#1c3450;text-align:center}
.stable-list__rows{margin-left:12px;width:393px;border-top:1px solid #fff}
.horse{display:grid;grid-template-columns:196px 197px;height:58.9px;border-bottom:2px solid #fff}
.horse__info{background:var(--cell);padding:7px 8px;border-right:2px solid #fff;font-size:6.2px;line-height:10px;color:#222}
.horse__box{font-size:6.6px}
.horse__name{font-weight:700;font-size:6.8px}
.horse__owner{background:var(--cell);display:flex;align-items:center;justify-content:center;text-align:center;font-size:8.2px;line-height:11px;padding:0 20px}
.silks{position:absolute;left:40px;top:118px;width:26px}
.silk{width:24px;height:44px;margin-bottom:15px;border-radius:10px 10px 7px 7px}
</style>
</head>
<body>

<section class="page page--left">
  <svg class="shapes" width="556" height="720" viewBox="0 0 556 720" aria-hidden="true">
    <polygon points="0,0 556,0 556,4 0,112" fill="var(--navy)"/>
    <polygon points="0,683 556,700 556,720 0,720" fill="var(--navy)"/>
    <polygon points="0,683 556,700 556,705 200,700" fill="var(--sky)"/>
  </svg>
  <div class="portrait" role="img" aria-label="Portrait photograph of trainer Rob Dawes outdoors"></div>
  <div class="brand"><span class="brand__dot"></span>Ashcombe Racing</div>

  <article class="welcome">
    <h1 class="welcome__title">Welcome to our 2016 Open Day</h1>
    <div class="welcome__body">
      <p>We have now been at Lower Ashcombe Farm for 2 years, and what a fantastic 2 seasons they have been! Last season we again achieved a personal best putting us in 30<sup>th</sup> position in the trainer’s title. We produced a total of 34 jumps winners plus 2 winners on the flat along with 30 second’s and 30 third’s which added up to over £340,000 in prize money, also our largest amount so far. This means the bar is raised again for the season ahead. It’s a daunting challenge at the start of the season but it’s the one target I set out to better each year; it won’t be easy but that’s my goal.</p>
      <p>This time last year I was expecting a bumper crop of Novice Chase winners but we had a change of plan early in the season to stay over hurdles with both The Chief’s Wish and Nineshadesofblue who went on to win 4 more races between them. Marlowsbar’s season had a late start due to a virus he picked up before winning over fences in impressive style at Eastcombe, then ran a terrific race in the Shires Marathon Chase to finish second carrying top weight. Delvany Duke finished second in 3 very competitive chases at Eastcombe, Ashworth and in a valuable race at Ulverley. What is particularly exciting, is that 3 of the above remain Novices for this season and the other will be aimed at the Great Downs Chase!</p>
      <p>Added to this Novice Chasing division for this season are dual winning hurdler You Don’t Say, the talented Amber Springs and Hallcroft Park who having had a wind operation should improve again over hurdles before going chasing.</p>
      <p>One of the most important parts of last season was to find ourselves playing on the bigger stage with Lil Moneybags. He has been flying the flag for the yard winning the £45,000 Grade 2 Hartwell Spirit Hurdle very impressively along with a £35,000 handicap at Sandhill. He then finished his season by running in no lesser race than the Premier Hurdle. He is currently being prepared for the Autumn Long Handicap on the 8<sup>th</sup> October and his target for the jumps season will be the Stayers’ Crown Hurdle at the Kingsbury Spring Festival.</p>
      <p>Both Oh Field Afire and Regimental should win a decent handicap hurdle before winter sets in. We have a good spread of nice Novice Hurdle prospects which include Bumper winners Fourth Manor, Deva Sapphire and Broad Pasture who was so impressive at Chepwell. Marella Flair and Shanmoor are two others I like that should find winning opportunities. Unstrapped, a 3 time winner last season will be aimed at Mares Listed Hurdles to try for that all important black type on her pedigree, whilst winning Irish Pointer Goodgirlmaria will run in Mares Hurdles this season.</p>
      <p>Of the Bumper horses, I hope Fourth Manor will be up to winning another and unraced horses Tollerton Lad and the 4yo by Whitlow’s Crown are two very nice types to look forward to this season.</p>
      <p>The ongoing success of the yard comes from the hard work and long hours which every member of our team puts in day in day out. The team is headed by Head Lad Daniel Foyle who joined us last November having previously worked in the same role for Graham Selby for 18 years. Hannah Reeve continues to do a sterling job of travelling our runners around the country backed up by Owen Marsh. I am very pleased to say Tom and Ravi are still going strong having started with me several years ago in Netherfield whilst Ellie and Jess are both hoping to have their first rides in amateur races for the yard. Kate Henley remains the voice on the end of the office phone, this is her second Open Day that she has prepared so well for us.</p>
      <p>Connor Bryce remains our stable jockey. Connor’s career keeps going from strength to strength and he and wife Lucy had a baby boy in July. Shane Dolan joined us as a conditional jockey a month ago having just ridden his first winner over hurdles. He currently claims 10lb when riding for us which will come in very handy.</p>
      <p>We’ve had another busy summer investing in the yard and improving the facilities. Our staff have been working with and around contractors, and clearing up behind them! A huge thank you to each and every one of them for their hard work.</p>
      <p>Finally thank you to all of our owners for your ongoing support and help in pushing the yard in the right direction, I hope this season is better again for everyone.</p>
      <p>Enjoy your day!</p>
    </div>
  </article>
  <div class="signature" role="img" aria-label="Handwritten signature of Rob Dawes"></div>
</section>

<section class="page page--right">
  <svg class="shapes" width="557" height="720" viewBox="0 0 557 720" aria-hidden="true">
    <polygon points="0,708 557,682 557,720 0,720" fill="var(--navy)"/>
    <polygon points="0,706 557,680 557,684 300,700" fill="var(--sky)"/>
  </svg>
  <div class="brand"><span class="brand__dot"></span>Ashcombe Racing</div>

  <div class="silks">
    <div class="silk" style="background:#1f9a3a" role="img" aria-label="Racing silks: green and blue"></div>
    <div class="silk" style="background:#1c2c5c" role="img" aria-label="Racing silks: navy with yellow cross and red sleeves"></div>
    <div class="silk" style="background:#a4203a" role="img" aria-label="Racing silks: maroon with blue and white hooped sleeves"></div>
    <div class="silk" style="background:#f0b4bf" role="img" aria-label="Racing silks: pink"></div>
    <div class="silk" style="background:#6fd12a" role="img" aria-label="Racing silks: lime green with dark dots"></div>
    <div class="silk" style="background:#f0b4bf" role="img" aria-label="Racing silks: pink"></div>
    <div class="silk" style="background:#1f8a34" role="img" aria-label="Racing silks: green with yellow cross"></div>
    <div class="silk" style="background:#e2261f" role="img" aria-label="Racing silks: red"></div>
    <div class="silk" style="background:#f2e032" role="img" aria-label="Racing silks: yellow with navy chevron"></div>
  </div>

  <div class="stable-list">
    <div class="stable-list__head"><span>Horses in Training</span><span>Barn A</span></div>
    <div class="stable-list__rows">
      <div class="horse"><div class="horse__info"><div class="horse__box">BOX 1</div><div class="horse__name">ELYSIAN KNIGHT (GB)</div><div>2011 Bay Gelding</div><div>Grand Boulevard ex Trinkora</div></div><div class="horse__owner">Mr Alan Frost</div></div>
      <div class="horse"><div class="horse__info"><div class="horse__box">BOX 2</div><div class="horse__name">SHANMOOR (IRE)</div><div>2011 Bay Gelding</div><div>Stowhill ex Shannow Run</div></div><div class="horse__owner">The Downland Racing For Fun Partnership</div></div>
      <div class="horse"><div class="horse__info"><div class="horse__box">BOX 3</div><div class="horse__name">GOLDEN STRAND (GB)</div><div>2010 Chesnut Gelding</div><div>Songbird Lane ex Alpen Rose</div></div><div class="horse__owner">Mrs Helen Carver</div></div>
      <div class="horse"><div class="horse__info"><div class="horse__box">BOX 4</div><div class="horse__name">GOODGIRLMARIA (IRE)</div><div>2010 Bay Mare</div><div>Marlow ex Wave Bay</div></div><div class="horse__owner">Mr &amp; Mrs P Holt</div></div>
      <div class="horse"><div class="horse__info"><div class="horse__box">BOX 5</div><div class="horse__name">STERLING PENNIES (IRE)</div><div>2012 Bay Filly</div><div>Cragmore ex Ten Penny Note</div></div><div class="horse__owner">Kestrel Lane Partnership</div></div>
      <div class="horse"><div class="horse__info"><div class="horse__box">BOX 6</div><div class="horse__name">YOU DON’T SAY (IRE)</div><div>2010 Bay Gelding</div><div>Marlow ex Wave Bay</div></div><div class="horse__owner">Mr Peter Holt &amp;<br>Mrs Jane Ashby</div></div>
      <div class="horse"><div class="horse__info"><div class="horse__box">BOX 7</div><div class="horse__name">MARLOWSBAR (IRE)</div><div>2009 Bay Gelding</div><div>Marlow ex Ardenvale</div></div><div class="horse__owner">Mr Robert Lyle</div></div>
      <div class="horse"><div class="horse__info"><div class="horse__box">BOX 8</div><div class="horse__name">DELVANY DUKE (GB)</div><div>2008 Bay Gelding</div><div>Kestrel Tor ex Little Sprig</div></div><div class="horse__owner">Mr and Mrs Charles Orton</div></div>
      <div class="horse"><div class="horse__info"><div class="horse__box">BOX 9</div><div class="horse__name">VILLAGE MOUSE (GB)</div><div>2010 Chesnut Gelding</div><div>Saraband ex Megvale</div></div><div class="horse__owner">Brian Pell and James Kerr</div></div>
    </div>
  </div>
</section>

</body>
</html>
```